Electric mountain bike tours nz

We are an Electric Mountain bike tour company in New Zealand. We will be offering bike rental and guided tours around the Nelson region in New Zealand. I want our website to represent both Mountain biking and New Zealand with the colours layout and features. We want tabs for the following:
-1 about us
-2 what we offer
-3 bookings/contact
Under the about us tab will be who we are as a a company. I want the ability to add videos to each of these tabs as we move foward with videos of the tracks we will be riding. I want the website to be editable so I can add and remove videos/photos myself. Also "our bikes" will be under this tab.
Under the what we offer tab will be
-1 bike rental and pricing
-2 guided tours and pricing
-3 recommended package deals.
I want to able to put the tracks under the guided tours tab and select beginner/ intermediate/advanced and have the tracks in each of the following to match the rider level. Also to be able to have a small video of the track would be great in this section.
Bookings and contact tab
(Further information for this tab to be updated soon)
Coded - Design and coding required
1 page
- Silver ferns, kiwi, mountains

```html
<!DOCTYPE html>
<html lang="en">
<head>
<meta charset="utf-8">
<title>TrailVolt – Electric Mountain Bike Tour NZ</title>
<link rel="stylesheet" href="https://fonts.googleapis.com/css2?family=Josefin+Sans:wght@600;700&family=Lato:ital,wght@0,400;0,700;1,400&display=swap">
<style>
:root{
  --ink:#111;
  --text:#555;
  --muted:#888;
  --line:#bdbdbd;
  --band:#f4f4f4;
  --white:#fff;
  --black:#000;
  --star:#f5b400;
  --map:#cfcfcf;
  --play-bg:rgba(20,20,20,.55);
}
*{margin:0;padding:0;box-sizing:border-box}
html,body{width:1200px;height:3309px;overflow:hidden}
body{position:relative;background:var(--white);font-family:"Lato",sans-serif;color:var(--text)}
.abs{position:absolute}
.head{font-family:"Josefin Sans",sans-serif;font-weight:700;color:var(--ink);text-transform:uppercase;letter-spacing:.5px}
.btn{position:absolute;display:flex;align-items:center;justify-content:center;width:141px;height:38px;border:2px solid var(--ink);border-radius:20px;font-size:14px;color:var(--ink);background:var(--white)}
.kicker{font-size:12px;color:var(--muted);font-style:italic}

/* hero */
.hero{left:0;top:0;width:1200px;height:740px;overflow:hidden}
.hero-photo{position:absolute;inset:0;background:linear-gradient(180deg,#46523a 0%,#5f6a4a 35%,#7d6c55 65%,#9a8a73 100%)}
.hero-shade{position:absolute;inset:0;background:rgba(0,0,0,.28)}
.hero-curve{position:absolute;left:0;bottom:0}
.nav{left:0;top:58px;width:1200px;height:40px;font-size:12px;color:var(--white)}
.nav span{position:absolute;top:12px}
.nav .active{background:var(--white);color:var(--ink);padding:3px 6px;top:9px}
.brand{display:flex;flex-direction:column;align-items:center;gap:6px}
.brand .dot{width:22px;height:22px;border-radius:50%;border:2px solid currentColor}
.brand .name{font-family:"Josefin Sans",sans-serif;font-weight:700;font-size:18px}
.hero-brand{left:540px;top:28px;width:120px;color:var(--white)}
.hero-title{left:0;width:1200px;text-align:center;color:var(--white)}
.hero-copy{left:330px;top:372px;width:540px;text-align:center;font-size:13px;line-height:18px;color:var(--white)}
.hero-btn{left:530px;top:430px;border-color:var(--white);background:transparent;color:var(--white)}

/* offers */
.offer-photo{width:222px;height:222px;border-radius:50%;border:6px solid var(--white);box-shadow:0 2px 8px rgba(0,0,0,.25)}
.offer-title{width:320px;text-align:center;font-size:18px;top:866px}
.offer-copy{width:230px;text-align:center;font-size:13px;line-height:17px;top:903px}

/* about */
.about{left:0;top:1152px;width:1200px;height:330px;background:var(--band)}
.about-video{left:615px;top:1152px;width:585px;height:330px;background:linear-gradient(160deg,#6f8aa3 0%,#4f5f44 45%,#7a6a4d 100%)}
.play{left:876px;top:1285px}
.about-copy{left:185px;width:390px;font-size:13px;line-height:17px;color:#333}

/* region */
.region-map{left:761px;top:1555px;width:276px;height:353px;background:var(--map);border-radius:40% 60% 45% 55%}
.region-title{left:185px;top:1640px;font-size:20px;line-height:27px}
.region-copy{left:185px;top:1728px;width:540px;font-size:13px;line-height:17px}

/* testimonials */
.reviews{left:0;top:1974px;width:1200px;height:431px;background:var(--band)}
.center{left:0;width:1200px;text-align:center}
.avatar{left:547px;top:2071px;width:106px;height:106px;border-radius:50%;border:5px solid var(--ink);background:linear-gradient(180deg,#8fb0cc,#4d6272)}
.quote{font-family:Georgia,serif;font-size:46px;color:var(--ink);font-weight:700}
.dots{left:578px;top:2370px;display:flex;gap:10px}
.dots i{width:7px;height:7px;border-radius:50%;background:#aaa}
.dots i:first-child{background:var(--ink)}

/* contact */
.field{border-bottom:1px solid var(--line);height:22px;font-size:11px;color:#999}

/* footer */
.footer{left:0;top:2905px;width:1200px;height:404px;background:var(--black);color:var(--white)}
.footer .abs{color:var(--white)}
.foot-brand{left:148px;top:50px;width:110px}
.foot-head{font-family:"Josefin Sans",sans-serif;font-weight:700;font-size:11px;text-transform:uppercase}
.foot-head::after{content:"";display:block;width:34px;height:1px;background:var(--white);margin-top:6px}
.foot-links{font-size:12px;line-height:42px}
.foot-links div::before{content:"";display:inline-block;width:8px;height:8px;border-radius:50%;border:2px solid var(--white);margin-right:14px;vertical-align:middle}
.tag{position:absolute;border:1px solid var(--white);font-size:11px;padding:3px 6px;height:22px}
.tag.on{background:#ddd;color:var(--ink)}
.insta{width:70px;height:64px}
.social{width:20px;height:20px;border-radius:50%;background:var(--white)}
</style>
</head>
<body>

<!-- hero -->
<header class="abs hero">
  <div class="hero-photo" role="img" aria-label="Orange electric mountain bike parked on a forest trail beside a track sign"></div>
  <div class="hero-shade"></div>
  <svg class="hero-curve" width="1200" height="180" viewBox="0 0 1200 180"><path d="M0 0 Q600 220 1200 0 L1200 180 L0 180 Z" fill="#fff"/></svg>
</header>
<nav class="abs nav">
  <span class="active" style="left:362px">Home</span>
  <span style="left:414px">What we offer ▾</span>
  <span style="left:685px">About us</span>
  <span style="left:748px">Bookings/Contact us</span>
</nav>
<div class="abs brand hero-brand"><span class="dot"></span><span class="name">TrailVolt</span></div>
<div class="abs hero-title head" style="top:282px;font-size:32px">Electric</div>
<div class="abs hero-title head" style="top:322px;font-size:44px">Mountain Bike Tour NZ</div>
<p class="abs hero-copy">Lorem Ipsum is simply dummy text of the printing and typesetting industry. Lorem Ipsum has been the industry's standard dummy text ever since the 1500s.</p>
<div class="btn hero-btn">Book Now</div>

<!-- offers -->
<div class="abs offer-photo" style="left:176px;top:606px;background:linear-gradient(160deg,#e6e0c4,#4a4a52)" role="img" aria-label="Row of rental e-bikes in a shop"></div>
<div class="abs offer-photo" style="left:487px;top:606px;background:linear-gradient(180deg,#9fb6cc,#5a6b7a 55%,#6b5a3a)" role="img" aria-label="Rider overlooking the bay on a guided tour"></div>
<div class="abs offer-photo" style="left:798px;top:606px;background:linear-gradient(160deg,#3a3a3a,#8a8a8a)" role="img" aria-label="Package of e-bikes lined up"></div>

<div class="abs head offer-title" style="left:127px">Bike Rental &amp; Pricing</div>
<div class="abs head offer-title" style="left:438px">Guided Tours &amp; Pricing</div>
<div class="abs head offer-title" style="left:749px;font-size:16px">Recommended Pakage Deals</div>
<p class="abs offer-copy" style="left:172px">Lorem Ipsum is simply dummy text of the printing and typesetting industry. Lorem Ipsum has been the industry's standard dummy text.</p>
<p class="abs offer-copy" style="left:483px">Lorem Ipsum is simply dummy text of the printing and typesetting industry. Lorem Ipsum has been the industry's standard dummy text.</p>
<p class="abs offer-copy" style="left:794px">Lorem Ipsum is simply dummy text of the printing and typesetting industry. Lorem Ipsum has been the industry's standard dummy text.</p>
<div class="btn" style="left:221px;top:992px">Read More</div>
<div class="btn" style="left:536px;top:992px">Read More</div>
<div class="btn" style="left:847px;top:992px">Read More</div>

<!-- about -->
<section class="abs about"></section>
<div class="abs about-video" role="img" aria-label="Video still of an orange e-bike on a hilltop track above the coast"></div>
<svg class="abs play" width="64" height="64" viewBox="0 0 64 64" aria-label="Play video"><circle cx="32" cy="32" r="30" fill="var(--play-bg)" stroke="#fff" stroke-width="2"/><path d="M26 20 L46 32 L26 44 Z" fill="#fff"/></svg>
<div class="abs kicker" style="left:185px;top:1196px">Who We Are</div>
<div class="abs head" style="left:185px;top:1214px;font-size:20px">About Us</div>
<p class="abs about-copy" style="top:1255px">Lorem Ipsum is simply dummy text of the printing and typesetting industry. Lorem Ipsum has been the industry's standard dummy text ever since the 1500s, when an unknown printer took a galley of type and scrambled it to make a type specimen book.</p>
<p class="abs about-copy" style="top:1333px">It has survived not only five centuries, but also the leap into electronic typesetting, remaining essentially unchanged.</p>
<div class="btn" style="left:185px;top:1400px">Read More</div>

<!-- region -->
<div class="abs region-map" role="img" aria-label="Map of New Zealand with the Nelson region highlighted"></div>
<div class="abs kicker" style="left:185px;top:1618px">Area Selection</div>
<div class="abs head region-title">Choose where you want<br>electrical mountain bike tour<br>in Nelson region</div>
<p class="abs region-copy">Lorem Ipsum is simply dummy text of the printing and typesetting industry. Lorem Ipsum has been the industry's standard dummy text ever since the 1500s, when an unknown printer took a galley of type and scrambled it to make a type specimen book.</p>
<div class="btn" style="left:185px;top:1840px">Book Now</div>

<!-- testimonials -->
<section class="abs reviews"></section>
<div class="abs center kicker" style="top:2004px">Testimonials</div>
<div class="abs center head" style="top:2022px;font-size:20px">Our Client's Says</div>
<div class="abs avatar" role="img" aria-label="Portrait of a rider in a helmet"></div>
<div class="abs center head" style="top:2200px;font-size:16px">Marcus Hale</div>
<div class="abs center" style="top:2222px;font-size:12px;color:var(--muted)">Rider</div>
<div class="abs quote" style="left:455px;top:2180px">“</div>
<p class="abs center" style="top:2248px;left:420px;width:360px;font-size:13px;line-height:17px;color:#333">Lorem Ipsum is simply dummy text of the printing and typesetting industry has Lorem Ipsum has been the on industry's standard dummy</p>
<div class="abs center" style="top:2300px;font-size:18px;color:var(--star)">★★★★★</div>
<div class="abs quote" style="left:700px;top:2280px">”</div>
<div class="abs dots"><i></i><i></i><i></i></div>

<!-- contact -->
<div class="abs center kicker" style="top:2486px">Contact Us</div>
<div class="abs center head" style="top:2504px;font-size:20px">Quick Contact</div>
<div class="abs field" style="left:271px;top:2570px;width:303px">Full Name</div>
<div class="abs field" style="left:629px;top:2570px;width:298px">Phone Number</div>
<div class="abs field" style="left:271px;top:2624px;width:656px">E-Mail Address</div>
<div class="abs field" style="left:271px;top:2680px;width:656px">Massage</div>
<div class="btn" style="left:530px;top:2768px">Send</div>

<!-- footer -->
<footer class="abs footer">
  <div class="abs brand foot-brand"><span class="dot"></span><span class="name">TrailVolt</span></div>
  <p class="abs" style="left:165px;top:148px;width:240px;font-size:12px;line-height:16px">Lorem Ipsum is simply dummy text ipsum is simply the dummy...</p>
  <div class="abs" style="left:165px;top:214px;font-size:12px;line-height:20px">
    <div>☎&nbsp; Phone: +64 3 555 0142</div>
    <div>✉&nbsp; hello@trailvolt.co.nz</div>
    <div>⚲&nbsp; Address : 12 Harbour Lane,<br>&nbsp;&nbsp;&nbsp;&nbsp;&nbsp;Nelson 7010</div>
  </div>

  <div class="abs foot-head" style="left:441px;top:96px">Quick Link</div>
  <div class="abs foot-links" style="left:441px;top:122px">
    <div>Home</div><div>About us</div><div>What we offer</div><div>Bookings/Contact us</div>
  </div>

  <div class="abs foot-head" style="left:638px;top:96px">Popular Tage</div>
  <span class="tag" style="left:638px;top:141px">Electric</span>
  <span class="tag" style="left:708px;top:141px">Bike</span>
  <span class="tag" style="left:778px;top:141px">Tour</span>
  <span class="tag" style="left:638px;top:200px">Comp..</span>
  <span class="tag" style="left:708px;top:200px">Services</span>
  <span class="tag" style="left:778px;top:200px">Deals</span>
  <span class="tag" style="left:638px;top:258px">Mountain</span>
  <span class="tag on" style="left:708px;top:258px">Cycle</span>

  <div class="abs foot-head" style="left:896px;top:96px">Instagram</div>
  <div class="abs insta" style="left:896px;top:144px;background:linear-gradient(135deg,#8a7a4a,#3d4a2a)" role="img" aria-label="Rider photo"></div>
  <div class="abs insta" style="left:970px;top:144px;background:linear-gradient(135deg,#6a7a5a,#a33a2a)" role="img" aria-label="Rider photo"></div>
  <div class="abs insta" style="left:896px;top:212px;background:linear-gradient(135deg,#9a8a5a,#4a5a3a)" role="img" aria-label="Rider photo"></div>
  <div class="abs insta" style="left:970px;top:212px;background:linear-gradient(135deg,#5a6a4a,#2a3020)" role="img" aria-label="Rider photo"></div>

  <div class="abs" style="left:165px;top:306px;width:874px;height:1px;background:#555"></div>
  <div class="abs" style="left:165px;top:333px;font-size:12px">Privacy policy · Legal mentions · Terms and Conditions</div>
  <div class="abs social" style="left:944px;top:332px"></div>
  <div class="abs social" style="left:966px;top:332px"></div>
  <div class="abs social" style="left:988px;top:332px"></div>
  <div class="abs social" style="left:1010px;top:332px"></div>
</footer>

</body>
</html>
```